Business Card Design Project

I require a business card with the following information on them for various different people;
name
m:
f:
e:
I have a logo already and will attached that. We are in the construction industry. I require something clean and simple but eye catching at the same time. You can use another colour with our logo if you like and you can style the logo as well if you wish. I am open.
Also it needs to be front and back design.
Industry/Entity Type
Construction
Requirements
Must have
- Logo, name, mobile, fax and email address.
Front and back design

```html
<!DOCTYPE html>
<html lang="en">
<head>
<meta charset="utf-8">
<title>Harbourstone Developments – Business Card</title>
<link rel="stylesheet" href="https://fonts.googleapis.com/css2?family=Marcellus&display=swap">
<style>
  :root {
    --card-bg: #e6e6e6;
    --card-bg-edge: #d4d4d4;
    --band-light: #9a9a9a;
    --band-dark: #5a5a5a;
    --skyline: #6e6e6e;
    --ink: #2b2b2b;
    --label-ink: #111111;
    --accent-green: #a8d58a;
  }
  html, body {
    margin: 0;
    padding: 0;
    width: 1200px;
    height: 748px;
    overflow: hidden;
    background: #ffffff;
  }
  .card {
    position: relative;
    width: 1200px;
    height: 748px;
    overflow: hidden;
    font-family: "Marcellus", serif;
  }
  .card__texture {
    position: absolute;
    inset: 0;
    background: radial-gradient(ellipse at 45% 55%, var(--card-bg) 55%, var(--card-bg-edge) 100%);
  }
  .brand-band {
    position: absolute;
    left: 0;
    top: 168px;
    width: 1200px;
    height: 96px;
    background: linear-gradient(90deg, var(--band-light) 0%, #808080 55%, var(--band-dark) 100%);
  }
  .skyline {
    position: absolute;
    left: 820px;
    top: 104px;
    width: 380px;
    height: 70px;
    background: linear-gradient(180deg, rgba(110,110,110,0.15) 0%, var(--skyline) 100%);
  }
  .brand-name {
    position: absolute;
    left: 46px;
    top: 40px;
    margin: 0;
    font-family: "Marcellus", serif;
    font-weight: 400;
    font-size: 108px;
    line-height: 1;
    letter-spacing: -1px;
    color: var(--ink);
  }
  .brand-sub {
    position: absolute;
    left: 58px;
    top: 186px;
    margin: 0;
    font-family: "Marcellus", serif;
    font-weight: 400;
    font-size: 54px;
    line-height: 1;
    letter-spacing: 18px;
    text-transform: uppercase;
    color: var(--ink);
  }
  .contact {
    position: absolute;
    left: 60px;
    top: 322px;
    display: grid;
    grid-template-columns: 190px 30px 600px;
    row-gap: 22px;
    font-size: 42px;
    line-height: 52px;
    color: var(--label-ink);
  }
  .contact__label { text-align: center; }
  .contact__colon { text-align: left; }
  .brand-square {
    position: absolute;
    left: 930px;
    top: 500px;
    width: 200px;
    height: 200px;
    background: var(--accent-green);
    opacity: 0.85;
  }
</style>
</head>
<body>
  <main class="card">
    <div class="card__texture" role="img" aria-label="Light grey geometric paper texture background"></div>

    <div class="skyline" role="img" aria-label="City skyline silhouette"></div>
    <div class="brand-band"></div>

    <h1 class="brand-name">Harbourstone</h1>
    <p class="brand-sub">Developments</p>

    <div class="contact">
      <span class="contact__label">Name</span><span class="contact__colon">:</span><span class="contact__value"></span>
      <span class="contact__label">Mobile</span><span class="contact__colon">:</span><span class="contact__value"></span>
      <span class="contact__label">Fax</span><span class="contact__colon">:</span><span class="contact__value"></span>
      <span class="contact__label">E-mail</span><span class="contact__colon">:</span><span class="contact__value"></span>
    </div>

    <div class="brand-square"></div>
  </main>
</body>
</html>
```